NURSING: RISING PAST THE SHADOWED SILL

Size of the book cover: 140 x 215 mms

I need a cover for the 30,000 word book I have just written. It is a positive take on what I think nursing is and what it needs to be in the future. It is also my story of being nursed and of being a nurse.

My dream is that nurses honor themselves; that they look to the future with confidence and intelligence and that care continues to be delivered with compassionate person centeredness.

I define nursing as a professional workforce which, with probity, prevent or relieve distress; provide compassionate, safe, excellent care; and which contributes to the organization of healthcare.

The name comes from a Biblical parable Corlan 3:7-9. If a light is hidden under a bushel (basket) it is barely seen. If it is lit out from the basket it is clearly seen. As nurses we must continue to take up our mantel and ensure our light is seen and that it continues to shine the way we want it to.

As nurses we each take up our own lantern of caring, each in our own ways. To walk more brightly in our own paths of service.

The final design should show the specialness of nursing.

Target Market(s)

Nurses present, past and future

Industry/Entity Type

Healthcare

Font styles to use
Sans Serif
Other font styles liked:
• Whatever you think will suit

Colors
ec1f27
0393ce
9bcb3c

Requirements
Must have
• Be friendly, calming.
• NB: I am not sure whether the title should be in uppercase or not. Nursing could be uppercase and rising past the shadowed sill could be lower case. I leave it to you experienced people
Nice to have
• Something that depicts nursing...or is suggestive of nursing and the specialness of the work we do. How we bring our light to our patients as we 'hold them in the palms of out hands' and care for them. How they honor us by allowing us into their lives. Our rich past and out history allows us to be who we are today and we look to the future with confidence and hope
• I like rich colors, eg the color type you might find on a stained glass window in a church - rich emerald green or rich crimson red or the deep blue of a nurses cape
Should not have
• A dark cover
• clutter
• Religious overtone
• I have chosen three colors but they are not in the shading I would like - see above

```html
<!DOCTYPE html>
<html lang="en">
<head>
<meta charset="utf-8">
<title>Nursing: Rising Past the Shadowed Sill — Cover Spread</title>
<link rel="stylesheet" href="https://fonts.googleapis.com/css2?family=Cormorant+Garamond:wght@300;400;500&family=Oswald:wght@400&display=swap">
<style>
  :root {
    --page-bg: #f0efd8;
    --back-bg: #2e3a38;
    --back-text: #d9ddd6;
    --about-bg: #3e4846;
    --spine-bg: #283432;
    --spine-accent: #a9b56b;
    --front-light: #c9cb82;
    --front-dark: #a6ab5b;
    --cross: #d29a5e;
    --title-red: #c1262c;
    --ink: #2c2f2a;
    --plate-dark: #2f4034;
    --plate-light: #8c9b7a;
    --avatar: #a9a9a9;
  }
  * { margin: 0; padding: 0; box-sizing: border-box; }
  html, body { width: 1200px; height: 900px; overflow: hidden; background: var(--page-bg); }
  .spread { position: relative; width: 1200px; height: 900px; }

  .back-cover {
    position: absolute; left: 10px; top: 12px; width: 647px; height: 796px;
    background: var(--back-bg);
  }
  .blurb {
    position: absolute; left: 34px; top: 32px; width: 466px;
    font-family: "Cormorant Garamond", serif; font-weight: 400;
    font-size: 14.4px; line-height: 15.5px; letter-spacing: 0.35px;
    color: var(--back-text); text-align: justify;
  }
  .blurb p { margin-bottom: 15.5px; }

  .about {
    position: absolute; left: 0; top: 618px; width: 533px; height: 178px;
    background: var(--about-bg);
  }
  .about-photo {
    position: absolute; left: 35px; top: 15px; width: 103px; height: 135px;
    background: linear-gradient(180deg, #ffffff 0%, #f2f2f2 100%);
  }
  .about-photo span {
    position: absolute; left: 14px; top: 14px; width: 75px; height: 121px;
    background: var(--avatar); border-radius: 36px 36px 0 0;
  }
  .about-heading {
    position: absolute; left: 165px; top: 18px;
    font-family: "Oswald", sans-serif; font-weight: 400; font-size: 13px;
    color: #eef0ea; letter-spacing: .3px;
  }
  .about-text {
    position: absolute; left: 165px; top: 47px; width: 350px;
    font-family: "Cormorant Garamond", serif; font-size: 14.4px; line-height: 15.5px;
    letter-spacing: 0.35px; color: var(--back-text); text-align: justify;
  }

  .spine {
    position: absolute; left: 543px; top: 12px; width: 114px; height: 796px;
    background: var(--spine-bg); overflow: hidden;
  }
  .spine-title {
    position: absolute; left: 43px; top: 33px; height: 562px;
    writing-mode: vertical-rl; transform: rotate(180deg);
    font-family: "Cormorant Garamond", serif; font-weight: 400;
    font-size: 23px; letter-spacing: 1px; line-height: 30px;
    color: var(--spine-accent); white-space: nowrap; text-align: center;
  }
  .spine-title .lead { color: var(--back-text); }
  .spine-author {
    position: absolute; left: 0; top: 692px; width: 114px; text-align: center;
    font-family: "Oswald", sans-serif; font-size: 21px; line-height: 25px;
    color: #ffffff; letter-spacing: .5px;
  }

  .front-cover {
    position: absolute; left: 657px; top: 12px; width: 543px; height: 796px;
    background: radial-gradient(ellipse at 55% 40%, var(--front-light) 0%, var(--front-dark) 100%);
    overflow: hidden;
  }
  .cross { position: absolute; background: var(--cross); opacity: .75; }
  .cross-v { left: 238px; top: 68px; width: 60px; height: 175px; }
  .cross-h { left: 178px; top: 123px; width: 175px; height: 60px; }
  .front-title {
    position: absolute; left: 56px; top: 80px; width: 470px;
    font-family: "Cormorant Garamond", serif; font-weight: 400;
    font-size: 90px; line-height: 100px; letter-spacing: 1px;
    color: var(--title-red); white-space: nowrap;
    transform: scaleY(1.2); transform-origin: 0 88px;
  }
  .front-subtitle {
    position: absolute; left: 60px; top: 180px; width: 440px;
    font-family: "Cormorant Garamond", serif; font-weight: 500;
    font-size: 36px; line-height: 40px; color: var(--ink); white-space: nowrap;
  }
  .plate {
    position: absolute; left: 133px; top: 276px; width: 267px; height: 367px;
  }
  .front-author {
    position: absolute; left: 0; top: 663px; width: 556px; text-align: center;
    font-family: "Cormorant Garamond", serif; font-weight: 500;
    font-size: 22px; letter-spacing: 7.5px; color: var(--ink);
  }
  .front-quote {
    position: absolute; left: 0; top: 709px; width: 556px; text-align: center;
    font-family: "Cormorant Garamond", serif; font-weight: 500;
    font-size: 15.5px; line-height: 20px; color: var(--ink);
  }
</style>
</head>
<body>
<main class="spread">
  <section class="back-cover">
    <div class="blurb">
      <p>Nursing is seldom expressed the way that it is in this book. It is written by a person who has been nursed or nursing all her life and it is recounted with honesty and candour. Every reader will find something to take from this narrative and nurses will no doubt see something of their own life mirrored in the many anecdotes and stories.</p>
      <p>Nursing: rising past the shadowed sill is a book which brings into the light the authors rich experience of the world and work of nursing. Through its words it subtly challenges individual nurses to think deeply about what ‘being a nurse’ means to them.</p>
      <p>What nurses do is a very big deal. Nurses choose to be nurses. No one tells them they have to do it but for some reason they decide to. The people they care for honour them by allowing them into their lives at what can be the most vulnerable and dramatic times of their life. How nurses position themselves, how they ‘walk’ with their patients, how they connect and care for them has consequences both for those in their care and for themselves.</p>
      <p>One of nursing’s unique realities is that the work crosses normal social boundaries. It is work that is not easily talked about outside of nursing, and the support nurses provide for each other is important in enabling them to remain healthy and able.</p>
      <p>Nursing has a rich history. Adela Thornbury lit her lantern of caring more than a century ago. The light from that lantern continues to glow and it is relit every moment of everyday by nurses all around the world as they go about their work.</p>
      <p>This book is more than just a story of nursing. It is the story and chronology of a professional life, intermingled with the telling of personal accounts and experiences. It also includes some special thoughts on nursing now and into the future. Nursing in the present day, presents many new challenges and opportunities. The workforce is one which adapts well to new ideas and situations. The future of nursing is in nurses hands and as such it can look to the future with confidence and pride.</p>
      <p>The writer salutes nurses everywhere.</p>
    </div>
    <div class="about">
      <div class="about-photo" role="img" aria-label="Author portrait placeholder"><span></span></div>
      <h2 class="about-heading">About the&nbsp; Writer</h2>
      <p class="about-text">Marion Hale is a Lorem ipsum dolor sit amet, consectetuer adipiscing elit, sed diam nonummy nibh euismod tincidunt ut laoreet dolore magna aliquam erat volutpat. Ut wisi enim ad minim veniam. Duis autem vel eum iriure dolor in hendrerit in vulputate velit esse molestie consequat</p>
    </div>
  </section>

  <section class="spine">
    <div class="spine-title"><span class="lead">NURSING:</span> RISING PAST THE SHADOWED SILL</div>
    <div class="spine-author">MARION<br>HALE</div>
  </section>

  <section class="front-cover">
    <div class="cross cross-v"></div>
    <div class="cross cross-h"></div>
    <h1 class="front-title">NURSING</h1>
    <p class="front-subtitle">Rising past the Shadowed Sill</p>
    <svg class="plate" viewBox="0 0 267 367" role="img" aria-label="Engraved illustration of a nurse in a veil offering a cup to a patient">
      <defs>
        <linearGradient id="plateTone" x1="0" y1="0" x2="0" y2="1">
          <stop offset="0" stop-color="#8c9b7a"/>
          <stop offset="0.5" stop-color="#5d6f55"/>
          <stop offset="1" stop-color="#2f4034"/>
        </linearGradient>
      </defs>
      <path d="M2 365 V60 Q2 2 60 2 H207 Q265 2 265 60 V365 Z" fill="url(#plateTone)" stroke="#2f4034" stroke-width="3"/>
    </svg>
    <p class="front-author">MARION HALE</p>
    <p class="front-quote">“We each take up our own lantern of caring, each in our own ways,<br>to walk more brightly in our own path of service.”</p>
  </section>
</main>
</body>
</html>
```